Venlow Vaults -responsive, bootstrap website design

Looking to build a responsive service website.

Logo and pictures have been provided.

PLEASE REVIEW ATTACHED DESIGN STYLE GUIDES & CLIENT CREATIVE BRIEF FOR OUR REQUIREMENT. THANK YOU AND GOOD LUCK!
Updates

Industry/Entity Type

Build

```html
<!DOCTYPE html>
<html lang="en">
<head>
<meta charset="utf-8">
<title>Venlow Vaults</title>
<link href="https://fonts.googleapis.com/css2?family=Josefin+Sans:wght@300;400&display=swap" rel="stylesheet">
<style>
:root{
  --bg:#1a1816;
  --page:#2a2622;
  --line:#8d8a86;
  --text:#d8d5d0;
  --muted:#9a968f;
  --accent:#b8473f;
  --price:#8c3a32;
  --modal:#0e0d0c;
}
*{box-sizing:border-box;margin:0;padding:0}
html,body{width:1200px;height:997px;overflow:hidden}
body{position:relative;background:var(--bg);font-family:"Josefin Sans",sans-serif;font-weight:300;color:var(--text)}
.abs{position:absolute}
.scene-bg{left:0;top:0;width:1200px;height:997px;background:linear-gradient(180deg,#1e1c1b 0%,#2b2a25 35%,#3a3528 70%,#2a2720 100%)}
.hero-bottle{left:184px;top:16px;width:128px;height:300px;background:linear-gradient(90deg,#151413,#3a3734 50%,#151413);border-radius:40px 40px 4px 4px}
.cart{left:800px;top:17px;font-size:12px;color:var(--muted);display:flex;align-items:center;gap:10px}
.checkout{left:944px;top:12px;width:72px;height:24px;border:1px solid var(--line);outline:1px solid var(--line);outline-offset:-4px;font-size:11px;text-align:center;line-height:25px;color:var(--muted)}
.brand{left:506px;top:45px;width:188px;height:144px;border:1px solid var(--line);border-radius:12px;display:flex;flex-direction:column;align-items:center;justify-content:center;color:var(--muted)}
.brand-name{font-size:26px;font-weight:400}
.brand-sub{font-size:7px;letter-spacing:2px;margin-top:8px;border-top:1px solid var(--line);padding-top:6px}
.social{top:104px;width:27px;height:27px;border:1px solid var(--line);outline:1px solid var(--line);outline-offset:-4px}
.nav{left:184px;top:234px;width:832px;height:35px;border-top:1px solid var(--line);border-bottom:1px solid var(--line);display:flex;justify-content:space-between;align-items:center;padding-top:4px;font-size:15px;color:var(--muted)}
.slider{left:184px;top:316px;width:546px;height:340px;background:linear-gradient(180deg,#5a4a4e 0%,#6a5a52 30%,#3f4a2c 60%,#2c3520 100%)}
.slide-arrow{width:28px;height:28px;border:1px solid #cfcac2;border-radius:50%;display:flex;align-items:center;justify-content:center}
.welcome{left:320px;top:453px;width:250px;height:66px;border:1px solid var(--line);font-size:20px;padding:10px 0 0 24px;color:#cfcac2}
.featured{left:184px;top:606px;width:546px;text-align:center;font-size:14px;color:#d6d1c8}
.dots{left:437px;top:640px;display:flex;gap:4px}
.dots span{width:8px;height:8px;border-radius:50%;background:#bbb}
.tile{left:754px;width:262px;height:180px}
.tile-label{left:71px;top:77px;width:112px;height:40px;border:1px solid #d3cec6;outline:1px solid #d3cec6;outline-offset:-4px;text-align:center;line-height:42px;font-size:18px;color:#e2ddd6}
.product{left:184px;top:674px;width:546px;height:214px;background:#34302b}
.product-bottle{left:84px;top:26px;width:66px;height:164px;background:linear-gradient(90deg,#0e0d0d,#353231 50%,#0e0d0d);border-radius:18px 18px 3px 3px}
.product-copy{left:213px;top:36px;width:270px;font-size:10.5px;line-height:18px;color:#c9c4bc}
.price{left:215px;top:153px;font-size:14px;color:var(--price)}
.add-cart{left:377px;top:144px;width:100px;height:33px;border:1px solid var(--line);outline:1px solid var(--line);outline-offset:-4px;text-align:center;line-height:35px;font-size:13px;color:#d2cdc5}
.footer{left:184px;top:934px;width:832px;border-top:1px solid var(--line);font-size:10px;color:var(--muted)}
.shade{left:0;top:0;width:1200px;height:997px;background:rgba(8,7,6,.76)}
.modal{left:334px;top:324px;width:532px;height:194px;background:var(--modal);border:1px solid #bdb9b3;outline:1px solid #bdb9b3;outline-offset:-5px}
.modal-title{left:0;top:20px;width:100%;text-align:center;font-size:14px;font-weight:400;color:#f2efe9}
.modal-text{left:100px;top:56px;width:332px;text-align:center;font-size:11.5px;line-height:18px;color:#eeeae4}
.age{left:38px;top:76px;font-size:30px;color:#fff}
.select{top:102px;width:80px;height:26px;border:1px solid #cfcbc5;outline:1px solid #cfcbc5;outline-offset:-4px;font-size:11px;color:#fff;display:flex;align-items:center;justify-content:space-between;padding:2px 10px 0 22px}
.options{left:146px;top:132px;width:80px;border:1px solid #cfcbc5;background:var(--modal)}
.options div{height:24px;border:1px solid #cfcbc5;margin:1px 2px;text-align:center;line-height:26px;font-size:11px;color:#fff}
.enter{left:242px;top:148px;width:82px;height:24px;border:1px solid var(--accent);outline:1px solid var(--accent);outline-offset:-4px;text-align:center;line-height:25px;font-size:10px;color:var(--accent)}
</style>
</head>
<body>
<div class="abs scene-bg" role="img" aria-label="Vineyard rows at dusk, full-page background photo"></div>
<div class="abs hero-bottle" role="img" aria-label="Wine bottle photo"></div>

<div class="abs cart">
  <svg width="12" height="11" viewBox="0 0 12 11" fill="none" stroke="#9a968f"><path d="M0 1h2l2 6h6l1-4H3"/><circle cx="5" cy="9.5" r="1"/><circle cx="9" cy="9.5" r="1"/></svg>
  <span>0 Product(s) - $0,00</span>
</div>
<div class="abs checkout">Checkout</div>

<div class="abs brand"><div class="brand-name">Venlow Vaults</div><div class="brand-sub">MARREN RIDGE VALLEY</div></div>

<div class="abs social" style="left:882px"></div>
<div class="abs social" style="left:918px"></div>
<div class="abs social" style="left:953px"></div>
<div class="abs social" style="left:989px"></div>

<nav class="abs nav"><span>Home</span><span>Story</span><span>Wine</span><span>Online Shop</span><span>News</span><span>Contact</span><span>Join The Venlow Family</span></nav>

<div class="abs slider" role="img" aria-label="Vineyard path photo slideshow"></div>
<div class="abs slide-arrow" style="left:196px;top:472px"><svg width="8" height="10"><path d="M6 1L2 5l4 4" stroke="#ddd" fill="none"/></svg></div>
<div class="abs slide-arrow" style="left:690px;top:472px"><svg width="8" height="10"><path d="M2 1l4 4-4 4" stroke="#ddd" fill="none"/></svg></div>
<div class="abs welcome">Welcome to Venlow Vaults<br>&nbsp;- Marren Ridge</div>
<div class="abs featured">Featured Products</div>
<div class="abs dots"><span></span><span></span><span></span><span></span></div>

<div class="abs tile" style="top:316px;background:linear-gradient(180deg,#6b5a48,#4a5530)" role="img" aria-label="Vineyard hills photo"><div class="abs tile-label">Vineyards</div></div>
<div class="abs tile" style="top:512px;background:linear-gradient(135deg,#3a2a1c,#6b4a2c,#2a1e14)" role="img" aria-label="Wine bottles on racks photo"><div class="abs tile-label">Shop Wines</div></div>
<div class="abs tile" style="top:709px;background:linear-gradient(135deg,#8a7452,#5a4832,#9a8460)" role="img" aria-label="Pile of wine corks photo"><div class="abs tile-label">Join Us</div></div>

<div class="abs product">
  <div class="abs slide-arrow" style="left:12px;top:93px;width:22px;height:22px"><svg width="8" height="10"><path d="M6 1L2 5l4 4" stroke="#ddd" fill="none"/></svg></div>
  <div class="abs slide-arrow" style="left:514px;top:93px;width:22px;height:22px"><svg width="8" height="10"><path d="M2 1l4 4-4 4" stroke="#ddd" fill="none"/></svg></div>
  <div class="abs product-bottle" role="img" aria-label="Red wine bottle product photo"></div>
  <p class="abs product-copy">Mauris gravida, nibh at vulputate mattis, diam urna aliquam ante, sit amet<br>blandit magna dui sed nisl. Phasellus interdum sollicitudin euismod.<br>Vestibulum a tortor eleifend, luctus purus at, placerat.</p>
  <div class="abs price">$49,99 (1,5l)</div>
  <div class="abs add-cart">Add to Cart</div>
</div>

<footer class="abs footer">
  <span class="abs" style="left:0;top:16px;white-space:nowrap">©2014 Venlow Vaults - All Rights Reserved.</span>
  <span class="abs" style="left:336px;top:16px;white-space:nowrap">Marren Ridge Valley, Oregon</span>
  <span class="abs" style="left:688px;top:16px;white-space:nowrap"><svg width="10" height="10" viewBox="0 0 10 10"><path d="M2 0l2 2-1 2 3 3 2-1 2 2-2 2C4 10 0 6 0 2z" fill="#9a968f"/></svg>&nbsp;&nbsp;(555) 204 - 381 - 0927</span>
  <span class="abs" style="left:688px;top:38px;white-space:nowrap"><svg width="10" height="8" viewBox="0 0 10 8"><rect x=".5" y=".5" width="9" height="7" fill="none" stroke="#9a968f"/><path d="M.5 .5l4.5 4 4.5-4" fill="none" stroke="#9a968f"/></svg>&nbsp;&nbsp;contact@venlowvaults.com</span>
</footer>

<div class="abs shade"></div>

<section class="abs modal" aria-label="Age Confirmation">
  <h2 class="abs modal-title">Age Confirmation</h2>
  <p class="abs modal-text">Please confirm you are at least 21 years of age by entering your birth date bellow.</p>
  <div class="abs age">+21</div>
  <div class="abs select" style="left:146px">29<svg width="9" height="6"><path d="M1 5l3.5-3.5L8 5" stroke="#fff" stroke-width="1.6" fill="none"/></svg></div>
  <div class="abs select" style="left:242px">June<svg width="9" height="6"><path d="M1 1l3.5 3.5L8 1" stroke="#fff" stroke-width="1.6" fill="none"/></svg></div>
  <div class="abs select" style="left:338px">2014<svg width="9" height="6"><path d="M1 1l3.5 3.5L8 1" stroke="#fff" stroke-width="1.6" fill="none"/></svg></div>
  <div class="abs options"><div>25</div><div>26</div><div>27</div><div>28</div><div>29</div></div>
  <div class="abs enter">ENTER</div>
</section>
</body>
</html>
```